We need a business card design for a new soccer program based in Melbourne, Victoria, Australia.
Coaching kids from 2 through to 14 develop social, motor and soccer skills, in a fun and friendly non-competitive environment.
Our company colours are blue and orange as seen in the logo attached below. However, we are happy for the font to be any modern colour that looks professional.
Target Market(s)
Mums and dads
Industry/Entity Type
Business
Contact Information for Business Card
business name: Bright Kick Soccer
Marko Delvino Director- 0451 738 015
Luke Ferrano Director- 0419 856 371
Tomas Kovalenko Head Coach
email: marko@brightkicksoccer.com.au
website: www.brightkicksoccer.com.au
Coaching kids from 2-14
https://www.facebook.com/brightkicksoccer (facebook page not required unless it looks good without being clustered)
Look and feel

```html
<!DOCTYPE html>
<html lang="en">
<head>
<meta charset="utf-8">
<title>Bright Kick Soccer – Business Card</title>
<link rel="stylesheet" href="https://fonts.googleapis.com/css2?family=Varela+Round&family=Fredoka:wght@600&display=swap">
<style>
  :root {
    --backdrop: #dcdcdc;
    --backdrop-light: #ececec;
    --grass: #2f7f22;
    --grass-dark: #25691a;
    --orange: #f29a1c;
    --purple: #4b2c88;
    --card-white: #eeeeee;
    --ink-white: #ffffff;
  }
  * { box-sizing: border-box; margin: 0; padding: 0; }
  html, body { width: 1200px; height: 750px; overflow: hidden; }
  body {
    background: radial-gradient(ellipse at 50% 30%, var(--backdrop-light), var(--backdrop));
    font-family: "Varela Round", sans-serif;
    position: relative;
  }
  .card {
    position: absolute;
    top: 232px;
    width: 500px;
    height: 286px;
    border-radius: 24px;
    overflow: hidden;
    box-shadow: 0 6px 18px rgba(0,0,0,0.18);
  }
  .card--front { left: 70px; }
  .card--back { left: 630px; background: var(--card-white); display: flex; }

  .pitch-art {
    position: absolute;
    inset: 0;
    background: radial-gradient(ellipse at center, var(--grass), var(--grass-dark));
  }

  .brand {
    display: flex;
    align-items: center;
    gap: 10px;
    font-family: "Fredoka", sans-serif;
    font-weight: 600;
  }
  .brand__dot { width: 24px; height: 24px; border-radius: 50%; flex: none; }
  .brand__name { line-height: 1.05; }

  .card--front .brand {
    position: absolute;
    left: 50%; top: 50%;
    transform: translate(-50%, -50%);
    white-space: nowrap;
  }
  .card--front .brand__dot { background: var(--ink-white); }
  .card--front .brand__name { color: var(--orange); font-size: 28px; }

  .back__identity {
    width: 44%;
    padding: 0 18px 0 24px;
    display: flex;
    flex-direction: column;
    justify-content: center;
    gap: 12px;
  }
  .back__identity .brand__name { color: var(--purple); font-size: 30px; }
  .back__identity .brand__dot { background: var(--purple); }
  .tagline { color: var(--orange); font-family: "Fredoka", sans-serif; font-weight: 600; font-size: 15px; white-space: nowrap; }

  .back__contacts {
    flex: 1;
    background: radial-gradient(ellipse at center, var(--grass), var(--grass-dark));
    padding: 26px 18px;
    display: flex;
    flex-direction: column;
    color: var(--orange);
    font-size: 14px;
    white-space: nowrap;
  }
  .person { margin-bottom: 8px; }
  .person__name { display: block; }
  .person__role { display: block; color: var(--ink-white); font-size: 8px; letter-spacing: 1px; margin: 1px 0 2px; }
  .contact-line { display: flex; align-items: center; gap: 6px; }
  .icon { width: 13px; height: 13px; flex: none; }
  .email { margin-top: 2px; font-size: 12.5px; }
  .website { margin-top: auto; font-size: 13px; }
</style>
</head>
<body>

<section class="card card--front" aria-label="Card front">
  <div class="pitch-art" role="img" aria-label="Grass soccer pitch with white field markings"></div>
  <div class="brand">
    <span class="brand__dot"></span>
    <span class="brand__name">Bright Kick Soccer</span>
  </div>
</section>

<section class="card card--back" aria-label="Card back">
  <div class="back__identity">
    <div class="brand">
      <span class="brand__dot"></span>
      <span class="brand__name">Bright<br>Kick<br>Soccer</span>
    </div>
    <p class="tagline">Coaching kids from 2-14</p>
  </div>

  <div class="back__contacts">
    <div class="person">
      <span class="person__name">Marko Delvino</span>
      <span class="person__role">DIRECTOR</span>
      <span class="contact-line">
        <svg class="icon" viewBox="0 0 16 16"><path fill="var(--ink-white)" d="M3 2h3l1.5 3.5-2 1.3a8 8 0 0 0 3.7 3.7l1.3-2L14 10v3a1 1 0 0 1-1 1A11 11 0 0 1 2 3a1 1 0 0 1 1-1z"/></svg>
        0451 738 015
      </span>
    </div>
    <div class="person">
      <span class="person__name">Luke Ferrano</span>
      <span class="person__role">DIRECTOR</span>
      <span class="contact-line">
        <svg class="icon" viewBox="0 0 16 16"><path fill="var(--ink-white)" d="M3 2h3l1.5 3.5-2 1.3a8 8 0 0 0 3.7 3.7l1.3-2L14 10v3a1 1 0 0 1-1 1A11 11 0 0 1 2 3a1 1 0 0 1 1-1z"/></svg>
        0419 856 371
      </span>
    </div>
    <div class="person">
      <span class="person__name">Tomas Kovalenko</span>
      <span class="person__role">HEAD COACH</span>
    </div>
    <span class="contact-line email">
      <svg class="icon" viewBox="0 0 16 16" fill="none" stroke="var(--ink-white)" stroke-width="1.6"><circle cx="8" cy="8" r="2.6"/><path d="M10.6 8v1.2a1.8 1.8 0 0 0 3.6 0V8a6.2 6.2 0 1 0-2.4 4.9"/></svg>
      marko@brightkicksoccer.com.au
    </span>
    <span class="contact-line website">
      <svg class="icon" viewBox="0 0 16 16"><path fill="var(--ink-white)" d="M3 2l10 5-4.2 1.2L11 13l-1.8.8-2.2-4.6L3 12z"/></svg>
      www.brightkicksoccer.com.au
    </span>
  </div>
</section>

</body>
</html>
```